Business card for pediatric occupational therapist

I need a business card design for my independent occupational therapy company. I am a pediatric occupational therapist working with children 0-3 years of age. I would like the card to be clean (not too 'busy') and can include pictures/cartoon-like images of children, or toys such as building blocks, or other images that would be relevant to pediatric therapy. I want it to look professional but also intended to be clear that services provided are for children.
Target Market(s)
Families requiring occupational therapy services for their children (physical, emotional, social needs) - developmental delays
Industry/Entity Type
Rehabilitation
Contact Information for Business Card
Maren Tolsvik OT LLC
Maren Tolsvik, OTR/L
Occupational Therapist
maren.tolsvikOT@brindlemail.com

```html
<!DOCTYPE html>
<html lang="en">
<head>
<meta charset="utf-8">
<title>Maren Tolsvik OT LLC — Business Card</title>
<link href="https://fonts.googleapis.com/css2?family=Montserrat:wght@400;500;700&display=swap" rel="stylesheet">
<style>
  :root {
    --canvas: #e4e0da;
    --card: #ffffff;
    --orange: #f07f1e;
    --orange-deep: #ef8444;
    --amber: #f7a93a;
    --yellow: #fbd85a;
    --peach-pale: #fbe3d3;
    --cream-pale: #fdf1dc;
    --shadow: rgba(60, 50, 40, 0.18);
  }
  * { box-sizing: border-box; margin: 0; padding: 0; }
  html, body {
    width: 1200px;
    height: 800px;
    overflow: hidden;
  }
  body {
    background: var(--canvas);
    font-family: "Montserrat", sans-serif;
    display: flex;
    align-items: center;
    justify-content: center;
    gap: 60px;
  }
  .card {
    position: relative;
    width: 525px;
    height: 300px;
    background: var(--card);
    box-shadow: 0 14px 30px var(--shadow);
    overflow: hidden;
  }
  .card__pattern {
    position: absolute;
    left: 0;
    top: 0;
    width: 100%;
    height: 118px;
  }
  .card--front .card__pattern {
    background: linear-gradient(90deg,
      var(--amber) 0%, var(--orange-deep) 20%, var(--yellow) 30%,
      var(--orange-deep) 40%, var(--peach-pale) 48%, var(--cream-pale) 75%, var(--peach-pale) 100%);
  }
  .card--front .card__pattern-tail {
    position: absolute;
    left: 28px;
    top: 118px;
    width: 108px;
    height: 70px;
    background: linear-gradient(180deg, var(--orange-deep), var(--amber));
  }
  .card--back .card__pattern {
    background: linear-gradient(90deg,
      var(--cream-pale) 0%, var(--peach-pale) 30%, var(--cream-pale) 55%, var(--peach-pale) 80%, var(--cream-pale) 100%);
  }
  .company-name {
    position: absolute;
    right: 28px;
    bottom: 34px;
    color: var(--orange);
    font-size: 26px;
    font-weight: 700;
    letter-spacing: 0.2px;
  }
  .company-name__suffix {
    font-weight: 500;
    font-size: 21px;
    margin-left: 4px;
  }
  .identity {
    position: absolute;
    left: 36px;
    top: 148px;
    color: var(--orange);
  }
  .identity__name {
    font-size: 22px;
    font-weight: 700;
    line-height: 1.05;
  }
  .identity__title {
    font-size: 9.5px;
    font-weight: 400;
    letter-spacing: 2.2px;
  }
  .contact-list {
    position: absolute;
    left: 36px;
    top: 210px;
    list-style: none;
    color: var(--orange);
    font-size: 12px;
    font-weight: 500;
  }
  .contact-list__item {
    display: flex;
    align-items: center;
    gap: 12px;
    margin-bottom: 8px;
  }
  .contact-list__icon {
    width: 11px;
    height: 11px;
    flex: none;
  }
</style>
</head>
<body>
  <section class="card card--front" aria-label="Card front">
    <div class="card__pattern" role="img" aria-label="Decorative band of interlocking jigsaw puzzle pieces in orange, yellow and pale peach"></div>
    <div class="card__pattern-tail" role="img" aria-label="Loose orange jigsaw puzzle pieces"></div>
    <p class="company-name">Maren Tolsvik<span class="company-name__suffix">OT LLC</span></p>
  </section>

  <section class="card card--back" aria-label="Card back">
    <div class="card__pattern" role="img" aria-label="Faint band of pale peach and cream jigsaw puzzle pieces"></div>
    <div class="identity">
      <h1 class="identity__name">Maren Tolsvik</h1>
      <p class="identity__title">Occupational Therapist</p>
    </div>
    <ul class="contact-list">
      <li class="contact-list__item">
        <svg class="contact-list__icon" viewBox="0 0 12 12" aria-hidden="true">
          <rect x="0.5" y="2" width="11" height="8" fill="var(--orange)"/>
          <path d="M0.5 2 L6 6.5 L11.5 2" fill="none" stroke="#fff" stroke-width="1"/>
        </svg>
        <span>maren.tolsvikOT@brindlemail.com</span>
      </li>
      <li class="contact-list__item">
        <svg class="contact-list__icon" viewBox="0 0 12 12" aria-hidden="true">
          <circle cx="6" cy="6" r="5.5" fill="var(--orange)"/>
          <path d="M0.5 6 H11.5 M6 0.5 V11.5 M6 0.5 C2.5 3.5 2.5 8.5 6 11.5 M6 0.5 C9.5 3.5 9.5 8.5 6 11.5" fill="none" stroke="#fff" stroke-width="0.8"/>
        </svg>
        <span>maren.tolsvik.com</span>
      </li>
    </ul>
  </section>
</body>
</html>
```